Bright and beautiful business card for a coach

I'm a personal and business coach based in Perth, Australia. I need a business card that whilst subtle and elegant, will stand out and appeal on a table full of cards.

My business name is Tide Mentoring and the business card must represent the warmth and brightness implied in the name, without being gimmicky. It must have a warmth and appeal and be easy to read.

I prefer clean, minimalist designs.

It must align with the feel of my website and socials: https://www.tidementoring.com.au/
https://www.instagram.com/tidementoringau/
https://www.facebook.com/tidementoringau
Updates

Hi Designers Thank you so much for taking the time to submit designs. I wonder if I could have explained myself a little better. Most of the designs that have been submitted look rather formal and many have quite corporate looking embellishments on them (to my eye). I would like softer, warmer, more organic. I’m open to people playing about and being more abstract, using softer embellishments (e.g the line drawing flowers and grasses I’ve used in my socials) incorporating other colours from my palette or like the social icons in my email signature (in PDF), perhaps playing with size/oversize, playing with the bleed. Please don’t be constrained by what I’ve already done, it merely needs to compliment. I’m sorry if I’m not using the right words or have led you astray. I’m no designer, but I’ve done my website, socials, email signature etc all myself (my logo was a design contest) and I was really hoping for my business card to be something more creative than I could have made with a template. Reminder: No black cards/sides please. Thank you 😊

Target Market(s)

Individuals, most likely but not all female. Creative thinkers. Likely professionals.

Industry/Entity Type

Business & Personal Coach

Contact Information for Business Card

(Tide Mentoring Logo) Name: Maren Delsby; Title: Business & Personal Coach; Phone number: +61 (0)438 915307; Email: maren@tidementoring.com.au; Website: https://tidementoring.com.au; Social icons for Facebook, Instagram & LinkedIn: @tidementoringAU. Optional strapline: "A thinking partner to help you cut through the noise"

Font styles to use
Sans Serif

Colors
00AB8E
00BBA5
67D7C9
C6EFE9
E9F9F6
59FF00
82FF00
B8FF75
E3FFCB
F4FFEA
FFC000
F8CF3A
FAE287
FDF2CF
FEFAEE

Requirements
Must have
• Must align with feel of my website and socials. Must have a pop of #FFC000 (possibly whole of one side, or at least a block). Bright or white background. Easy to read.
Nice to have
• Possibly incorporate the sunshine/grass picture I have used in website and socials - will upload.
Should not have
• Must not be black or dark. Not impersonal or corporate looking.

```html
<!DOCTYPE html>
<html lang="en">
<head>
<meta charset="utf-8">
<title>Tide Mentoring – Business Card</title>
<link rel="stylesheet" href="https://fonts.googleapis.com/css2?family=Poppins:wght@400;500&display=swap">
<style>
  :root {
    --backdrop: #8c8c8c;
    --card-front: #e2e1e4;
    --card-back: #eeb40f;
    --ink: #161616;
    --brand: #b97a2b;
    --rule: #f2b418;
    --social-dot: #ececec;
  }
  * { margin: 0; padding: 0; box-sizing: border-box; }
  html, body { width: 1200px; height: 1101px; overflow: hidden; }
  body {
    position: relative;
    background: var(--backdrop);
    font-family: "Poppins", sans-serif;
    color: var(--ink);
  }
  .card { position: absolute; width: 302px; height: 530px; }
  .card-front { left: 246px; top: 268px; background: var(--card-front); }
  .card-back { left: 641px; top: 267px; background: var(--card-back); }

  .brand-name {
    position: absolute; left: 40px; top: 92px;
    font-size: 27px; font-weight: 500; color: var(--brand);
    letter-spacing: 0.5px; white-space: nowrap;
  }
  .holder-name {
    position: absolute; left: 32px; top: 263px;
    font-size: 20px; font-weight: 500; letter-spacing: 1.6px;
  }
  .rule { position: absolute; left: 30px; width: 228px; height: 1.5px; background: var(--rule); }
  .rule-name { top: 295px; width: 226px; }
  .rule-contact { top: 415px; }
  .holder-title {
    position: absolute; left: 31px; top: 303px;
    font-size: 14px; letter-spacing: 0.2px;
  }
  .contact-icons { position: absolute; left: 36px; top: 384px; display: flex; gap: 20px; align-items: center; }
  .contact-icons svg { display: block; }
  .contact-list {
    position: absolute; left: 32px; top: 429px;
    list-style: none; font-size: 15px; line-height: 19.5px;
  }

  .quote-mark {
    position: absolute; left: 32px; top: 30px;
    font-size: 46px; font-weight: 500; line-height: 1;
  }
  .strapline {
    position: absolute; left: 32px; top: 75px;
    font-size: 15.5px; line-height: 19.2px; letter-spacing: 0.3px;
  }
  .social-dots { position: absolute; left: 28px; top: 435px; display: flex; gap: 10px; }
  .social-dots span { width: 27px; height: 27px; border-radius: 50%; background: var(--social-dot); }
  .social-handle {
    position: absolute; left: 30px; top: 470px;
    font-size: 15px; letter-spacing: 0.3px;
  }
</style>
</head>
<body>
  <section class="card card-front">
    <div class="brand-name">Tide Mentoring</div>
    <h1 class="holder-name">MAREN DELSBY</h1>
    <div class="rule rule-name"></div>
    <p class="holder-title">BUSINESS &amp; PERSONAL COACH</p>
    <div class="contact-icons">
      <svg width="19" height="19" viewBox="0 0 24 24" aria-label="Phone"><path fill="#161616" d="M6.6 10.8c1.4 2.8 3.8 5.1 6.6 6.6l2.2-2.2c.3-.3.7-.4 1-.2 1.1.4 2.3.6 3.6.6.6 0 1 .4 1 1V20c0 .6-.4 1-1 1C10.6 21 3 13.4 3 4c0-.6.4-1 1-1h3.5c.6 0 1 .4 1 1 0 1.3.2 2.5.6 3.6.1.3 0 .7-.2 1l-2.3 2.2z"/></svg>
      <svg width="24" height="16" viewBox="0 0 24 16" aria-label="Email"><rect width="24" height="16" fill="#161616"/><path d="M1 1l11 8 11-8" fill="none" stroke="#e2e1e4" stroke-width="1.6"/></svg>
      <svg width="19" height="19" viewBox="0 0 24 24" aria-label="Website"><g fill="none" stroke="#161616" stroke-width="1.8"><circle cx="12" cy="12" r="10"/><ellipse cx="12" cy="12" rx="4.5" ry="10"/><path d="M2 12h20M4 6.5h16M4 17.5h16"/></g></svg>
    </div>
    <div class="rule rule-contact"></div>
    <ul class="contact-list">
      <li>+61 (0)438 915307</li>
      <li>maren@tidementoring.com.au</li>
      <li>www.tidementoring.com.au</li>
    </ul>
  </section>

  <section class="card card-back">
    <div class="quote-mark">&ldquo;</div>
    <p class="strapline">A thinking<br>partner to help<br>you cut through<br>the noise</p>
    <div class="social-dots"><span></span><span></span><span></span></div>
    <p class="social-handle">@tidementoringAU</p>
  </section>
</body>
</html>
```